COOL PROJECT: Modern and Elegant Design for a Luxury Home Cleaning Company

We're looking for an elegant car wrap design for a Home Cleaning company based in Miami called The Velora Maids. We clean homes for medium to wealthy people and we want to attract this audience.

The design should communicate trust, professionalism & expertise. While looking SEXY!

Specs:
- Car Model: Corvane Strada K Sport Trim 2021(I included a picture)
- Our Logo Font: Dosis Extra Bold(But if you have another cool font you want to test, we are open to other ideas)
- Please ensure to use the same colors as in the logo

Information to include on the car:
a. Slogan Options:
MORE THAN JUST A CLEANING
or
VELORA GLOW, DAY AFTER DAY

b. Our Website www.theveloramaidshq.co

c. (305) 555 - 0148

d. I also included a few stamp design files, feel free to use these if you think it could look cool somewhere(Files: Stamp 1, stamp 2, stamp 3)

HAVE FUN!

```html
<!DOCTYPE html>
<html lang="en">
<head>
<meta charset="utf-8">
<title>The Velora Maids – Vehicle Wrap</title>
<link href="https://fonts.googleapis.com/css2?family=Dosis:wght@600;700;800&display=swap" rel="stylesheet">
<style>
  :root {
    --brand-yellow: #f0b323;
    --brand-navy: #1e3a4c;
    --brand-navy-dark: #162d3c;
    --brand-white: #ffffff;
    --page-bg: #ffffff;
  }
  * { box-sizing: border-box; margin: 0; padding: 0; }
  html, body {
    width: 1200px;
    height: 1200px;
    overflow: hidden;
    background: var(--page-bg);
    font-family: "Dosis", sans-serif;
  }
  .canvas {
    position: relative;
    width: 1200px;
    height: 1200px;
  }
  .wrap-panel {
    position: absolute;
    left: 50px;
    width: 1100px;
    height: 500px;
    border-radius: 28px;
    overflow: hidden;
    background: var(--brand-yellow);
  }
  .wrap-panel--primary { top: 60px; }
  .wrap-panel--alternate { top: 640px; }
  .wrap-graphic {
    position: absolute;
    inset: 0;
    width: 100%;
    height: 100%;
  }
  .brand-lockup {
    position: absolute;
    left: 80px;
    top: 110px;
    display: flex;
    align-items: flex-end;
    gap: 16px;
  }
  .brand-mark {
    width: 72px;
    height: 72px;
    background: var(--brand-navy);
    border-radius: 6px;
  }
  .brand-name {
    font-weight: 800;
    font-size: 62px;
    line-height: 0.88;
    color: var(--brand-navy);
    text-transform: uppercase;
  }
  .website {
    position: absolute;
    left: 80px;
    bottom: 34px;
    font-weight: 700;
    font-size: 28px;
    color: var(--brand-white);
    white-space: nowrap;
  }
  .phone {
    position: absolute;
    font-weight: 700;
    font-size: 32px;
    line-height: 1;
    color: var(--brand-yellow);
    letter-spacing: 0.5px;
    white-space: nowrap;
  }
  .slogan {
    position: absolute;
    font-weight: 800;
    text-transform: uppercase;
    line-height: 1;
    white-space: nowrap;
  }
  .slogan-line {
    display: inline-block;
    font-size: 40px;
    padding: 4px 12px;
    background: var(--brand-navy-dark);
  }
  .slogan-line--lead {
    color: var(--brand-white);
    border-radius: 8px 8px 0 0;
  }
  .slogan-line--follow {
    color: var(--brand-yellow);
    border-radius: 0 8px 8px 8px;
  }
  .stamp-row {
    position: absolute;
    display: flex;
    gap: 16px;
  }
  .stamp {
    width: 46px;
    height: 46px;
    border-radius: 50%;
    background: var(--brand-yellow);
    border: 4px solid var(--brand-navy-dark);
    box-shadow: 0 0 0 2px var(--brand-yellow);
  }
  .wrap-panel--primary .phone { left: 730px; top: 252px; }
  .wrap-panel--primary .slogan { left: 720px; top: 300px; }
  .wrap-panel--primary .stamp-row { left: 920px; top: 175px; }
  .wrap-panel--alternate .phone { left: 865px; top: 205px; }
  .wrap-panel--alternate .slogan { left: 700px; top: 270px; }
  .wrap-panel--alternate .stamp-row { left: 712px; top: 395px; }
</style>
</head>
<body>
<main class="canvas">

  <section class="wrap-panel wrap-panel--primary" aria-label="Side wrap, version one">
    <svg class="wrap-graphic" viewBox="0 0 1100 500" preserveAspectRatio="none" aria-hidden="true">
      <path d="M0,380 C260,380 520,345 690,250 C850,160 970,50 1100,20" fill="none" stroke="#ffffff" stroke-width="12"/>
      <path d="M0,398 C260,398 530,362 705,265 C865,175 985,65 1100,38 V500 H0 Z" fill="#1e3a4c"/>
      <path d="M760,470 C880,450 1000,430 1100,420" fill="none" stroke="#ffffff" stroke-width="10"/>
      <path d="M770,500 C880,478 1000,458 1100,450 V500 Z" fill="#f0b323"/>
    </svg>
    <div class="brand-lockup">
      <span class="brand-mark"></span>
      <h1 class="brand-name">The<br>Velora<br>Maids</h1>
    </div>
    <p class="website">www.theveloramaidshq.co</p>
    <p class="phone">(305) 555 - 0148</p>
    <p class="slogan">
      <span class="slogan-line slogan-line--lead">Velora Glow,</span><br>
      <span class="slogan-line slogan-line--follow">Day After Day</span>
    </p>
    <div class="stamp-row">
      <span class="stamp"></span><span class="stamp"></span><span class="stamp"></span>
    </div>
  </section>

  <section class="wrap-panel wrap-panel--alternate" aria-label="Side wrap, version two">
    <svg class="wrap-graphic" viewBox="0 0 1100 500" preserveAspectRatio="none" aria-hidden="true">
      <path d="M0,380 C260,380 520,345 690,250 C850,160 970,50 1100,20" fill="none" stroke="#ffffff" stroke-width="12"/>
      <path d="M0,398 C260,398 530,362 705,265 C865,175 985,65 1100,38 V500 H0 Z" fill="#1e3a4c"/>
      <path d="M760,470 C880,450 1000,430 1100,420" fill="none" stroke="#ffffff" stroke-width="10"/>
      <path d="M770,500 C880,478 1000,458 1100,450 V500 Z" fill="#f0b323"/>
    </svg>
    <div class="brand-lockup">
      <span class="brand-mark"></span>
      <h2 class="brand-name">The<br>Velora<br>Maids</h2>
    </div>
    <p class="website">www.theveloramaidshq.co</p>
    <p class="slogan">
      <span class="slogan-line slogan-line--lead">Velora Glow,</span><br>
      <span class="slogan-line slogan-line--follow">Day After Day</span>
    </p>
    <p class="phone">(305) 555 - 0148</p>
    <div class="stamp-row">
      <span class="stamp"></span><span class="stamp"></span><span class="stamp"></span>
    </div>
  </section>

</main>
</body>
</html>
```